High-end construction company needs a business card design

We need a modern looking business card that draws people in, is memorable and looks so good people will want to sick it on their fridges.
On the first side what is needed are:
Logo
My name - Tomas Verbelk
Title - Managing Director
Website - www.kravel.co.uk
Email - tomas@kravel.co.uk
Telephone - 020 5194 6381
Mobile - 07845319027
On the back side was is needed is a list of all the services we provide:
-Kitchen Renovations
-Bathroom Renovations
-House Renovations
-Garage Conversions
-Extensions
-Loft Conversions
-Conservatories
-Carpentry
-Tiling
-Electrical
-Plumbing & Heating
-Bricklaying
-Landscaping
-Decorating
-Plastering
We would like the colours to be the same shades as on the logo with grey or black for the words.
Target Market(s)
Anyone who needs building work done
Contact Information for Business Card
This business card is for a construction company which strives to deliver excellent service and quality.
The look and feel of the card should represent this.
Requirements
Must have
- On the first side what is needed are:
Logo
My name - Tomas Verbelk
Title - Managing Director
Website - www.kravel.co.uk
Email - tomas@kravel.co.uk
Telephone - 020 5194 6381
Mobile - 07845319027
Nice to have
- Cool looking features

```html
<!DOCTYPE html>
<html lang="en">
<head>
<meta charset="utf-8">
<title>Kravel Construction Ltd – Business Card</title>
<link rel="stylesheet" href="https://fonts.googleapis.com/css2?family=Poppins:wght@400;500;600;700&display=swap">
<style>
  :root {
    --green: #4fb233;
    --green-light: #76c84a;
    --green-dark: #3c9a2a;
    --ink: #3a3a3a;
    --paper: #ffffff;
    --backdrop: #2a2a2a;
  }
  * { box-sizing: border-box; margin: 0; padding: 0; }
  html, body {
    width: 1200px;
    height: 900px;
    overflow: hidden;
    background: var(--backdrop);
    font-family: "Poppins", sans-serif;
  }
  .sheet {
    width: 1200px;
    height: 900px;
    display: flex;
    flex-direction: column;
    align-items: center;
    justify-content: center;
    gap: 34px;
  }
  .card {
    width: 700px;
    height: 400px;
    border-radius: 4px;
    position: relative;
    overflow: hidden;
    box-shadow: 0 10px 30px rgba(0,0,0,.45);
  }

  /* Services side */
  .card--services {
    background: linear-gradient(135deg, var(--green-light) 0%, var(--green) 55%, var(--green-dark) 100%);
    color: var(--paper);
    display: flex;
    flex-direction: column;
    align-items: center;
    justify-content: center;
    text-align: center;
  }
  .brand-name {
    display: flex;
    align-items: center;
    gap: 12px;
    font-weight: 700;
    font-size: 34px;
    letter-spacing: .5px;
    line-height: 1;
  }
  .brand-mark {
    width: 18px;
    height: 18px;
    background: currentColor;
  }
  .card--services .brand-name { margin-bottom: 34px; }
  .service-list {
    list-style: none;
    font-size: 18px;
    font-weight: 500;
    line-height: 1.55;
  }

  /* Contact side */
  .card--contact {
    background: var(--paper);
    display: flex;
    align-items: center;
  }
  .contact-brand {
    width: 330px;
    display: flex;
    justify-content: center;
  }
  .contact-brand .brand-name {
    color: var(--green);
    font-size: 26px;
    flex-direction: column;
    gap: 10px;
    text-align: center;
  }
  .brand-name .brand-line { display: block; }
  .divider {
    width: 2px;
    height: 200px;
    background: var(--green);
  }
  .contact-details {
    padding-left: 46px;
  }
  .person-name {
    color: var(--green);
    font-weight: 600;
    font-size: 26px;
    line-height: 1.1;
  }
  .person-title {
    color: var(--ink);
    font-size: 15px;
    margin-bottom: 18px;
  }
  .contact-list { list-style: none; }
  .contact-item {
    display: flex;
    align-items: center;
    gap: 14px;
    color: var(--ink);
    font-size: 19px;
    line-height: 1.5;
  }
  .contact-icon {
    width: 20px;
    height: 20px;
    flex: none;
    fill: var(--green);
  }
</style>
</head>
<body>
<main class="sheet">

  <section class="card card--services" aria-label="Services side">
    <div class="brand-name">
      <span class="brand-mark"></span>
      <span>Kravel Construction Ltd</span>
    </div>
    <ul class="service-list">
      <li>Kitchen Renovations - Bathroom Renovations - House Renovations</li>
      <li>Garage Conversions - Extensions - Loft Conversions - Conservatories</li>
      <li>Carpentry - Tiling - Electrical - Plumbing &amp; Heating - Bricklaying</li>
      <li>Landscaping - Decorating - Plastering</li>
    </ul>
  </section>

  <section class="card card--contact" aria-label="Contact side">
    <div class="contact-brand">
      <div class="brand-name">
        <span class="brand-line">Kravel</span>
        <span class="brand-line">Construction Ltd</span>
      </div>
    </div>
    <div class="divider"></div>
    <div class="contact-details">
      <h1 class="person-name">Tomas Verbelk</h1>
      <p class="person-title">Managing Director</p>
      <ul class="contact-list">
        <li class="contact-item">
          <svg class="contact-icon" viewBox="0 0 24 24" aria-hidden="true"><path d="M6.6 10.8a15.1 15.1 0 0 0 6.6 6.6l2.2-2.2c.3-.3.7-.4 1-.2 1.1.4 2.3.6 3.6.6.6 0 1 .4 1 1V20c0 .6-.4 1-1 1A17 17 0 0 1 3 4c0-.6.4-1 1-1h3.5c.6 0 1 .4 1 1 0 1.3.2 2.5.6 3.6.1.3 0 .7-.2 1z"/></svg>
          <span>07845319027</span>
        </li>
        <li class="contact-item">
          <svg class="contact-icon" viewBox="0 0 24 24" aria-hidden="true"><path d="M3 8c0-2 4-4 9-4s9 2 9 4v2h-5V8H8v2H3zM6 12h12l2 8H4zm6 2a2.5 2.5 0 1 0 0 5 2.5 2.5 0 0 0 0-5z"/></svg>
          <span>020 5194 6381</span>
        </li>
        <li class="contact-item">
          <svg class="contact-icon" viewBox="0 0 24 24" aria-hidden="true"><path d="M2 5h20v14H2zm2 2v.4l8 5.2 8-5.2V7z"/></svg>
          <span>tomas@kravel.co.uk</span>
        </li>
        <li class="contact-item">
          <svg class="contact-icon" viewBox="0 0 24 24" aria-hidden="true"><path d="M12 2a10 10 0 1 0 0 20 10 10 0 0 0 0-20zm1 17.9V17h-2v2.9A8 8 0 0 1 4.1 13H7v-2H4.1A8 8 0 0 1 11 4.1V7h2V4.1a8 8 0 0 1 6.9 6.9H17v2h2.9a8 8 0 0 1-6.9 6.9z"/></svg>
          <span>www.kravel.co.uk</span>
        </li>
      </ul>
    </div>
  </section>

</main>
</body>
</html>
```